Web design for Modeling agency

We are looking for re-designing our modeling agency website.
Current website: brisamodels.com our competitor: QRTmodels.com
http://ravonmodel.fr/
https://www.dunforthmanagement.com/models/
https://www.hendra-models.de
https://www.fennmanagement.co.uk
https://www.vantrimodel.com
https://www.brackenfordmodels.com

Target Market(s)

modeling agency

Industry/Entity Type

modeling agency

Number of Pages Required

5+ page

Font styles to use
Other font styles liked:
• base on logo guidline

Requirements
Nice to have
• current website: brisamodels.com our competitor: QRTmodels.com

```html
<!DOCTYPE html>
<html lang="en">
<head>
<meta charset="utf-8">
<title>Brisa Models</title>
<link rel="stylesheet" href="https://fonts.googleapis.com/css2?family=Montserrat:wght@200;300;400;500;600;800&display=swap">
<style>
:root{
  --ink:#1f1a17;
  --muted:#4a4440;
  --accent:#b8998a;
  --accent-dark:#a3826f;
  --paper:#ffffff;
  --dark-1:#2a1a15;
  --dark-2:#5a4238;
  --dark-3:#9b7c6d;
}
*{box-sizing:border-box;margin:0;padding:0}
html,body{width:1200px;height:3501px;overflow:hidden;background:var(--paper)}
body{position:relative;font-family:'Montserrat',sans-serif;color:var(--ink)}
.abs{position:absolute}
.photo{position:absolute;overflow:hidden;box-shadow:inset 0 0 0 1px rgba(255,255,255,.15)}
.photo::after{content:"";position:absolute;inset:0;background:radial-gradient(ellipse at 50% 35%,rgba(255,255,255,.22),rgba(255,255,255,0) 60%),linear-gradient(180deg,rgba(0,0,0,0) 55%,rgba(0,0,0,.18) 100%)}

/* header */
.site-header{position:absolute;left:0;top:0;width:1200px;height:97px;background:var(--paper)}
.menu-icon{left:72px;top:42px;width:26px;height:16px}
.nav-link{position:absolute;top:42px;font-size:13px;letter-spacing:.5px;color:var(--muted)}
.nav-link.active{font-weight:600;color:var(--ink)}
.nav-link.active::after{content:"";position:absolute;left:0;right:0;top:22px;height:2px;background:var(--accent)}
.brand{position:absolute;left:490px;top:12px;width:200px;text-align:center;color:var(--accent-dark);font-weight:400}
.brand .word{display:block;font-size:40px;letter-spacing:3px;line-height:44px}
.brand .sub{display:block;font-size:17px;letter-spacing:1px;line-height:24px}
.login{position:absolute;left:1009px;top:33px;width:94px;height:33px;border:2px solid var(--muted);font-size:13px;text-align:center;line-height:29px;color:var(--muted)}

/* hero */
.hero-title{position:absolute;left:0;width:1200px;top:622px;text-align:center;font-size:114px;letter-spacing:1px;color:var(--accent);line-height:120px;white-space:nowrap}
.hero-title .strong{font-weight:800}
.hero-title .light{font-weight:200}
.rail-label{position:absolute;left:1128px;width:70px;text-align:center;transform:rotate(-90deg);font-size:9px;letter-spacing:1px;color:#fff}
.scroll-line{left:1162px;top:400px;width:1px;height:80px;background:#fff}
.scroll-text{left:1097px;top:530px;width:130px;transform:rotate(-90deg);font-size:10px;letter-spacing:2px;color:#fff;text-align:center}

/* section titles */
.section-title{position:absolute;left:0;width:1200px;text-align:center;font-size:32px;font-weight:300;letter-spacing:4px}
.section-title b{font-weight:800}
.section-title::after{content:"";position:absolute;left:571px;top:48px;width:58px;height:3px;background:var(--accent)}
.on-dark{color:#fff}

/* featured */
.model-name{position:absolute;font-size:14px;text-align:center;color:var(--muted);width:267px}
.model-date{position:absolute;font-size:12px;text-align:center;color:var(--muted);width:267px}

/* videos */
.videos{left:0;top:1307px;width:1200px;height:717px;background:linear-gradient(115deg,var(--dark-1) 0%,var(--dark-2) 55%,var(--dark-3) 100%)}
.play-label{position:absolute;left:69px;width:751px;top:1730px;text-align:center;font-size:22px;letter-spacing:5px;color:#fff}

/* news */
.news-caption{position:absolute;text-align:center;color:#fff;font-weight:600;font-size:15px;line-height:21px}
.news-caption .date{display:block;font-size:12px;letter-spacing:3px;font-weight:500;margin-bottom:2px}
.news-caption.featured{font-size:19px;line-height:27px}
.news-caption.featured .date{font-size:14px}
.learn-more{display:inline-block;margin-top:14px;border:2px solid #fff;padding:5px 24px;font-size:11px;font-weight:500;letter-spacing:1px;line-height:18px}

/* footer */
.site-footer{left:2px;top:3304px;width:1198px;height:197px;background:linear-gradient(100deg,var(--dark-1) 0%,var(--dark-2) 60%,var(--dark-3) 100%)}
.footer-link{position:absolute;top:3361px;font-size:11px;letter-spacing:.5px;color:#fff}
.copyright{position:absolute;left:0;width:1200px;top:3390px;text-align:center;font-size:11px;color:#e6dcd6}
.social-row{position:absolute;left:0;width:1200px;top:3428px;text-align:center;font-size:12px;font-weight:500;color:#fff;letter-spacing:.5px}
.social-row span{display:inline-block;margin:0 9px}
.social-row span::before{content:"";display:inline-block;width:9px;height:9px;border-radius:50%;background:#fff;margin-right:6px;vertical-align:0}
</style>
</head>
<body>

<header class="site-header">
  <svg class="abs menu-icon" viewBox="0 0 26 16"><g stroke="#6b625d" stroke-width="1.5"><line x1="0" y1="1" x2="26" y2="1"/><line x1="0" y1="8" x2="26" y2="8"/><line x1="0" y1="15" x2="26" y2="15"/></g></svg>
  <span class="nav-link active" style="left:170px">MEN</span>
  <span class="nav-link" style="left:251px">WOMEN</span>
  <span class="nav-link" style="left:358px">TALENT</span>
  <div class="brand"><span class="word">BRISA</span><span class="sub">MODELS</span></div>
  <span class="nav-link" style="left:733px">VIDEO</span>
  <span class="nav-link" style="left:828px">ABOUT</span>
  <span class="nav-link" style="left:929px">NEWS</span>
  <span class="login">LOGIN</span>
</header>

<section class="hero">
  <div class="photo" style="left:0;top:97px;width:380px;height:585px;background:linear-gradient(175deg,#efe2d3 0%,#eab08f 60%,#d98f6c 100%)" role="img" aria-label="Model in a peach belted dress"></div>
  <div class="photo" style="left:380px;top:97px;width:460px;height:585px;background:linear-gradient(175deg,#ece2d6 0%,#dccbb7 60%,#cdb8a1 100%)" role="img" aria-label="Model in profile wearing a beige blazer"></div>
  <div class="photo" style="left:840px;top:97px;width:360px;height:585px;background:linear-gradient(185deg,#e8d9c8 0%,#e6a685 60%,#d68e6b 100%)" role="img" aria-label="Smiling model in a peach dress"></div>
  <span class="rail-label" style="top:262px">LUMO</span>
  <span class="rail-label" style="top:302px">PIXA</span>
  <span class="rail-label" style="top:342px">CHIRP</span>
  <div class="abs scroll-line"></div>
  <div class="abs scroll-text">SCROLL DOWN ›</div>
  <div class="hero-title"><span class="strong">BRISA</span> <span class="light">MODELS</span></div>
</section>

<section class="featured">
  <h2 class="section-title" style="top:798px">FEATURED <b>MODLES</b></h2>
  <div class="photo" style="left:79px;top:886px;width:267px;height:264px;background:linear-gradient(160deg,#f1efec,#b9aea6)" role="img" aria-label="Male model portrait"></div>
  <div class="photo" style="left:349px;top:926px;width:266px;height:264px;background:linear-gradient(160deg,#d8c6b2,#a89079)" role="img" aria-label="Model seated in a wicker chair"></div>
  <div class="photo" style="left:617px;top:886px;width:267px;height:264px;background:linear-gradient(160deg,#e4e2e0,#6e5749)" role="img" aria-label="Model with natural curls"></div>
  <div class="photo" style="left:887px;top:918px;width:268px;height:264px;background:linear-gradient(160deg,#a9c4d2,#b0806f)" role="img" aria-label="Model in a veil against blue sky"></div>
  <div class="model-name" style="left:79px;top:1170px">DALIA MORREN &nbsp;|&nbsp; FW 2021</div>
  <div class="model-date" style="left:79px;top:1193px">13 OCT 2021</div>
  <div class="model-name" style="left:349px;top:1205px">DALIA MORREN &nbsp;|&nbsp; FW 2021</div>
  <div class="model-date" style="left:349px;top:1228px">13 OCT 2021</div>
  <div class="model-name" style="left:617px;top:1170px">DALIA MORREN &nbsp;|&nbsp; FW 2021</div>
  <div class="model-date" style="left:617px;top:1193px">13 OCT 2021</div>
  <div class="model-name" style="left:887px;top:1200px">DALIA MORREN &nbsp;|&nbsp; FW 2021</div>
  <div class="model-date" style="left:887px;top:1223px">13 OCT 2021</div>
</section>

<section class="abs videos"></section>
<h2 class="section-title on-dark" style="top:1354px">LATEST <b>VIDEOS</b></h2>
<div class="photo" style="left:69px;top:1442px;width:751px;height:497px;background:linear-gradient(90deg,#1f2a5c 0%,#333c6c 38%,#c99a3a 62%,#e0b35a 100%)" role="img" aria-label="Featured video: model leaning on a car by a yellow building"></div>
<svg class="abs" style="left:411px;top:1633px" width="80" height="80" viewBox="0 0 80 80"><circle cx="40" cy="40" r="36" fill="none" stroke="#fff" stroke-width="5"/><path d="M31 24 L57 40 L31 56 Z" fill="#fff"/></svg>
<div class="play-label">PLAY NOW</div>
<div class="photo" style="left:827px;top:1442px;width:316px;height:160px;background:linear-gradient(150deg,#c9b3a0,#6b5548)" role="img" aria-label="Video thumbnail: model with raised arms"></div>
<div class="photo" style="left:827px;top:1610px;width:316px;height:161px;background:linear-gradient(150deg,#d9b690,#5a4a50)" role="img" aria-label="Video thumbnail: two models posing"></div>
<div class="photo" style="left:827px;top:1778px;width:316px;height:161px;background:linear-gradient(150deg,#3a4556,#8a6a5e)" role="img" aria-label="Video thumbnail: close portrait of a model"></div>
<svg class="abs" style="left:966px;top:1501px" width="48" height="48" viewBox="0 0 48 48"><circle cx="24" cy="24" r="21" fill="none" stroke="#fff" stroke-opacity=".8" stroke-width="3"/><path d="M19 14 L34 24 L19 34 Z" fill="#fff" fill-opacity=".8"/></svg>
<svg class="abs" style="left:966px;top:1666px" width="48" height="48" viewBox="0 0 48 48"><circle cx="24" cy="24" r="21" fill="none" stroke="#fff" stroke-opacity=".8" stroke-width="3"/><path d="M19 14 L34 24 L19 34 Z" fill="#fff" fill-opacity=".8"/></svg>
<svg class="abs" style="left:966px;top:1834px" width="48" height="48" viewBox="0 0 48 48"><circle cx="24" cy="24" r="21" fill="none" stroke="#fff" stroke-opacity=".8" stroke-width="3"/><path d="M19 14 L34 24 L19 34 Z" fill="#fff" fill-opacity=".8"/></svg>

<section class="news">
  <h2 class="section-title" style="top:2085px">LATEST <b>NEWS</b></h2>
  <div class="photo" style="left:0;top:2165px;width:380px;height:363px;background:linear-gradient(170deg,#e9c09d,#4a3228)" role="img" aria-label="News: model with braided hair"></div>
  <div class="photo" style="left:385px;top:2165px;width:402px;height:363px;background:linear-gradient(170deg,#4a5370,#7d7486)" role="img" aria-label="News: model in a white ruffled gown"></div>
  <div class="photo" style="left:791px;top:2165px;width:409px;height:363px;background:linear-gradient(170deg,#5d5c50,#b0643e)" role="img" aria-label="News: model with long brown hair"></div>
  <div class="photo" style="left:0;top:2534px;width:384px;height:363px;background:linear-gradient(170deg,#9ba7b0,#2234a8)" role="img" aria-label="News: model in a blue tulle dress"></div>
  <div class="photo" style="left:389px;top:2534px;width:402px;height:363px;background:linear-gradient(170deg,#e7dccd,#c98aa3)" role="img" aria-label="News: model in a floral shirt"></div>
  <div class="photo" style="left:795px;top:2534px;width:405px;height:363px;background:linear-gradient(170deg,#d8d8d8,#3a3a3a)" role="img" aria-label="News: black and white close portrait"></div>

  <div class="news-caption" style="left:20px;width:340px;top:2454px"><span class="date">25 OCT 2021</span>LOREM IPSUM DOLOR SIT AMET CONSECTETUR</div>
  <div class="news-caption featured" style="left:405px;width:362px;top:2292px"><span class="date">25 OCT 2021</span>LOREM IPSUM DOLOR SIT AMET CONSECTETUR<br><span class="learn-more">LEARN MORE</span></div>
  <div class="news-caption" style="left:831px;width:330px;top:2454px"><span class="date">25 OCT 2021</span>LOREM IPSUM DOLOR SIT AMET CONSECTETUR</div>
  <div class="news-caption" style="left:22px;width:340px;top:2823px"><span class="date">25 OCT 2021</span>LOREM IPSUM DOLOR SIT AMET CONSECTETUR</div>
  <div class="news-caption" style="left:420px;width:340px;top:2823px"><span class="date">25 OCT 2021</span>LOREM IPSUM DOLOR SIT AMET CONSECTETUR</div>
  <div class="news-caption" style="left:827px;width:340px;top:2823px"><span class="date">25 OCT 2021</span>LOREM IPSUM DOLOR SIT AMET CONSECTETUR</div>
</section>

<section class="follow">
  <h2 class="abs" style="left:0;width:1200px;top:2955px;text-align:center;font-size:24px;font-weight:400;letter-spacing:3px">FOLLOW <b style="font-weight:800">US</b></h2>
  <div class="photo" style="left:60px;top:3022px;width:211px;height:183px;background:linear-gradient(160deg,#7a8a95,#3a3432)" role="img" aria-label="Social post: model in a check blazer"></div>
  <div class="photo" style="left:277px;top:3022px;width:211px;height:183px;background:linear-gradient(160deg,#cfc9c4,#8e9bb8)" role="img" aria-label="Social post: model in a pale blue gown"></div>
  <div class="photo" style="left:492px;top:3022px;width:211px;height:183px;background:linear-gradient(160deg,#3a2a1e,#c08a4a)" role="img" aria-label="Social post: model wearing glasses"></div>
  <div class="photo" style="left:706px;top:3022px;width:211px;height:183px;background:linear-gradient(160deg,#5a6a88,#b8482e)" role="img" aria-label="Social post: model in a red coat"></div>
  <div class="photo" style="left:922px;top:3022px;width:210px;height:183px;background:linear-gradient(160deg,#8a959c,#b85a3a)" role="img" aria-label="Social post: model in a red top"></div>
  <span class="abs" style="left:277px;width:211px;top:3104px;text-align:center;font-size:13px;font-weight:500;letter-spacing:1px;color:#fff">PIXA</span>
</section>

<footer class="abs site-footer"></footer>
<span class="footer-link" style="left:248px">MEN</span>
<span class="footer-link" style="left:345px">WOMEN</span>
<span class="footer-link" style="left:464px">TALENT</span>
<span class="footer-link" style="left:580px">VIDEO</span>
<span class="footer-link" style="left:688px">ABOUT</span>
<span class="footer-link" style="left:801px">NEWS</span>
<span class="footer-link" style="left:907px">CONTACT US</span>
<div class="copyright">copyright © 2021 brisa | All Rights Reserved</div>
<div class="social-row"><span>Lumo</span><span>Chirp</span><span>Vidra</span><span>Pixa</span></div>

</body>
</html>
```